wine label for ultra premium vineyard in Bendigo, Central Otago, New Zealand

"LARKSPUR" is our new wine brand, with grapes grown in our spectacular "ter Hoeven" vineyard. The small, elevated vineyard overlooks a river valley and snowy mountains. We would like a highly elegant label for our 2018 pinot noir wine, which highlights the quality of wine and our very special vineyard location. "LARKSPUR" has to be prominent, with secondary emphasis on "ter Hoeven vineyard" and "Bendigo, Central Otago". A stylized LARKSPUR logo (bird) could be a useful design device instead of the commonly seen illustrated mountain landscape (which is quite common for our local wines). Label size 90 high, 110 wide. Please use a pinot noir / burgundy bottle. See here for vineyard pics, and also below pics for other local wine labels and pics for inspiration / styles. https://www.instagram.com/jas.ter.hoeven.example/

Target Market(s)

average bottle price for this premium red pinot noir would be aroundUS$40. target market are generally urban professionals aged 25 and older with a high degree of interest in pinot noir wine, and who are familiar with New Zealand pinot noir (ie. already know several brands).

Colors
ed252d

Requirements
Must have
• distinctive label, sophisticated look
Nice to have
• classy white paper stock
Should not have
• label must not get too busy... less but high quality and distinctive is more....

```html
<!DOCTYPE html>
<html lang="en">
<head>
<meta charset="utf-8">
<title>LARKSPUR 2018 Pinot Noir – Label</title>
<link href="https://fonts.googleapis.com/css2?family=Cinzel:wght@400&family=Marcellus&family=Sacramento&family=Montserrat:wght@400&display=swap" rel="stylesheet">
<style>
  :root {
    --canvas-bg: #f6f6f6;
    --paper: #f0efed;
    --paper-shade: #e7e6e3;
    --burgundy: #8c1a2b;
    --script-red: #9c2437;
    --ink: #1c1c1c;
    --sketch-grey: #b4b4b4;
    --sketch-grey-deep: #9a9a9a;
    --sketch-rose: #d8a2a8;
  }
  * { margin: 0; padding: 0; box-sizing: border-box; }
  html, body {
    width: 1200px;
    height: 2796px;
    overflow: hidden;
    background: var(--canvas-bg);
  }
  .canvas {
    position: relative;
    width: 1200px;
    height: 2796px;
  }
  .label {
    position: absolute;
    left: 0;
    top: 907px;
    width: 1200px;
    height: 982px;
    background: radial-gradient(ellipse at 50% 40%, var(--paper) 55%, var(--paper-shade) 100%);
    text-align: center;
  }
  .label > * {
    position: absolute;
    left: 0;
    width: 100%;
  }
  .brand {
    top: 56px;
    font-family: "Cinzel", serif;
    font-weight: 400;
    font-size: 158px;
    line-height: 1;
    letter-spacing: 14px;
    color: var(--burgundy);
  }
  .illustration {
    top: 218px;
    left: 345px;
    width: 495px;
    height: 420px;
  }
  .vintage {
    top: 650px;
    font-family: "Marcellus", serif;
    font-size: 48px;
    line-height: 1;
    color: var(--ink);
  }
  .varietal {
    top: 708px;
    font-family: "Marcellus", serif;
    font-weight: 400;
    font-size: 80px;
    line-height: 1;
    letter-spacing: 4px;
    color: var(--ink);
  }
  .vineyard {
    top: 786px;
    font-family: "Sacramento", cursive;
    font-size: 84px;
    line-height: 1;
    color: var(--script-red);
  }
  .region {
    top: 880px;
    font-family: "Montserrat", sans-serif;
    font-weight: 400;
    font-size: 44px;
    line-height: 1;
    letter-spacing: 3px;
    color: var(--ink);
  }
</style>
</head>
<body>
<main class="canvas">
  <section class="label">
    <h1 class="brand">LARKSPUR</h1>
    <svg class="illustration" role="img" aria-label="Pencil illustration of a small bird perched beside a nest among wild roses, with soft red watercolour blooms" viewBox="0 0 495 420">
      <defs>
        <linearGradient id="sketch-tone" x1="0" y1="0" x2="1" y2="1">
          <stop offset="0%" stop-color="var(--sketch-grey)"/>
          <stop offset="45%" stop-color="var(--sketch-rose)"/>
          <stop offset="100%" stop-color="var(--sketch-grey-deep)"/>
        </linearGradient>
      </defs>
      <ellipse cx="247" cy="210" rx="238" ry="202" fill="url(#sketch-tone)" fill-opacity="0.55"/>
    </svg>
    <p class="vintage">2018</p>
    <h2 class="varietal">PINOT NOIR</h2>
    <p class="vineyard">ter Hoeven vineyard</p>
    <p class="region">Bendigo, Central Otago</p>
  </section>
</main>
</body>
</html>
```